Modern Velaris company

We need a new company presentation brochure, composed of about 20 pages in A4 format.
Cover, page 1 who we are, page 2 company profile, page 3 territorial operation, page from 4 to 10 services offered and description of services (The title of the page are: Perizie e Liquidazione danni, riparazioni e sostituzioni, teleclaimer, accertamento danni da fenomeno elettrico, TPA, Auditing, drone pilot, Valutazione rischi), from 11 to 17 specializations (Sinistri gravi, R.C., Tecnologici, Energie rinnovabili, strutture, ambiente) page 18 e 19 integrated services (perdite occulte, ricerca guasti, indagini termografiche, crisis management), page 20 clients ( list companies and logos) page 21 contact.
The company is made up of various companies, which belong to the principal, each of which deals with specific activities.
To date we already have various logos of the main company (Vardano and Pescetti) as well as the logos of the other companies. I load them on the portal.
Found then the graphic solution that we like we will have to proceed to make a presentation in similar powerpoint and the website.

Target Market(s)

Insurance Company, Insurance Broker

Font styles to use
Other font styles liked:
• ARIAL

Colors
333333
5c5c5c
959595
0392cd

Requirements
Must have
• It must be clear, professional and modern.
Nice to have
• I indicate some competitor sites, so that you can better understand what we are doing. www.torvellsgroup.example, www.harbridgeoakes.example, www.betadomaretti.example, www.gruppotavesi.example, www.vantuzzi.example.

```html
<!DOCTYPE html>
<html lang="it">
<head>
<meta charset="utf-8">
<title>Vardano &amp; Pescetti – Brochure</title>
<link rel="stylesheet" href="https://fonts.googleapis.com/css2?family=Arimo:wght@400;700&display=swap">
<style>
:root{
  --ink:#333333;
  --ink-soft:#5c5c5c;
  --ink-light:#959595;
  --blue:#0392cd;
  --blue-deep:#1f74bd;
  --orange:#e8731c;
  --panel:#f0f0f0;
  --page:#ffffff;
  --stage:#e6e6e6;
  --photo-dark:#2e2e2e;
}
*{box-sizing:border-box;margin:0;padding:0}
html,body{width:1200px;height:1003px;overflow:hidden;background:var(--stage);font-family:"Arimo",Arial,sans-serif;color:var(--ink)}
.spread{position:absolute;left:230px;width:740px;height:477px;background:var(--page);box-shadow:0 2px 8px rgba(0,0,0,.18);overflow:hidden}
.spread--outside{top:16px}
.spread--inside{top:510px}
.abs{position:absolute}
.fold{position:absolute;left:370px;top:0;width:1px;height:100%;background:rgba(0,0,0,.06)}
.title{font-weight:700;color:var(--orange);font-size:12px;letter-spacing:.2px}
.brand{font-size:13px;color:var(--blue-deep);font-weight:400;white-space:nowrap}
.brand small{display:block;font-size:5px;color:var(--ink-light);letter-spacing:.3px}
.brand--lg{font-size:15px}
.sub{font-size:8px;font-weight:700;color:var(--orange);line-height:1.2}
.list{list-style:none;font-size:6px;line-height:1.35;color:var(--ink-soft)}
.list li{position:relative;padding-left:9px;margin-bottom:5px}
.list li::before{content:"";position:absolute;left:1px;top:2.5px;width:3px;height:3px;border-radius:50%;background:var(--blue)}
.list b{color:var(--ink)}
.list--tight li{margin-bottom:0}
.cell{position:absolute}
.cell--grey{background:var(--panel)}
.badge{position:absolute;background:#cfd3d6}
.footer-band{position:absolute;left:0;top:413px;width:370px;height:64px;background:var(--blue-deep)}
.addr{position:absolute;color:#fff;font-size:5.5px;line-height:1.35}
.addr b{display:block;color:#9fcff0;font-size:5px;letter-spacing:.5px;margin-bottom:2px}
.seal{position:absolute;left:304px;top:420px;width:44px;height:44px;border-radius:50%;background:#e9eef3;border:3px solid #fff}
.stripe{position:absolute;left:370px;bottom:0;width:370px;height:8px;background:var(--blue-deep)}
.stripe::after{content:"";position:absolute;right:0;top:0;width:70px;height:8px;background:var(--orange);clip-path:polygon(12% 0,100% 0,100% 100%,0 100%)}
.stripe--left{left:0}
.photo{position:absolute}
.cover-photo{left:370px;top:105px;width:370px;height:305px;background:linear-gradient(135deg,#5a5a5a 0%,#2b2b2b 55%,#1c1c1c 100%)}
.cover-text{position:absolute;left:38px;color:#fff;font-weight:700;font-size:10px;letter-spacing:.2px;line-height:1.25}
.url{position:absolute;font-size:7px;color:var(--ink-soft)}
.letter{position:absolute;left:0;top:38px;width:370px;height:102px;background:var(--panel)}
.letter p{position:absolute;font-size:6px;line-height:1.3;color:var(--ink)}
.insurers{position:absolute;left:24px;top:172px;width:240px;display:grid;grid-template-columns:repeat(4,60px);grid-auto-rows:26px;column-gap:10px}
.insurers span{font-size:8.5px;font-weight:700;color:var(--blue-deep);display:flex;align-items:center}
.territory{position:absolute;left:0;top:314px;width:370px;height:163px;background:var(--blue-deep)}
.territory p{position:absolute;left:24px;top:16px;width:100px;color:#fff;font-size:7px;line-height:1.3}
.map{position:absolute;top:14px;height:120px;background:#fff}
.map div{position:absolute;inset:3px}
.studio-note{position:absolute;left:562px;top:44px;width:154px;height:90px;background:var(--blue);color:#fff;font-size:5.8px;line-height:1.3;padding:4px 5px}
.studio-note p+p{margin-top:5px}
.body-small{position:absolute;font-size:6px;line-height:1.35;color:var(--ink-soft)}
.sign{position:absolute;font-size:5.5px;color:var(--orange);font-weight:700;text-align:center;width:70px}
.sign i{display:block;margin-top:6px;height:1px;background:var(--ink-light)}
</style>
</head>
<body>

<!-- Outside spread: structure + cover -->
<section class="spread spread--outside">
  <div class="fold"></div>

  <h2 class="title abs" style="left:18px;top:18px">LA STRUTTURA</h2>

  <div class="cell cell--grey" style="left:0;top:44px;width:180px;height:146px"></div>
  <div class="cell cell--grey" style="left:180px;top:190px;width:190px;height:162px"></div>

  <div class="abs" style="left:18px;top:54px">
    <div class="brand">Vardano &amp; Pescetti<small>consulenza tecnica per le assicurazioni</small></div>
    <p class="sub" style="margin-top:10px">Divisione sinistri<br>Property e Liability</p>
    <ul class="list" style="margin-top:6px;width:150px">
      <li><b>Gestione perizie Rami Elementari</b> (massa e complessi) nonché da Responsabilità civile (R.C.G. ed R.C.O.)</li>
      <li>Svolgiamo consulenza tecnica in sede di A.t.p. e cause civili ed accertamenti tecnici in caso di infortuni e lesioni.</li>
    </ul>
  </div>

  <div class="abs" style="left:198px;top:54px">
    <div class="brand brand--lg" style="font-weight:700">T.R.V.<small>Technical Review Valuations</small></div>
    <p class="sub" style="margin-top:14px">Indennizzo in forma specifica</p>
    <ul class="list" style="margin-top:6px;width:150px">
      <li>Divisione dedicata con personale interno per esecuzione diagnosi strumentale per l'individuazione della rottura degli impianti.</li>
      <li><b>Operiamo con varie Mandanti per la gestione dei sinistri con "Indennizzo in forma specifica".</b></li>
    </ul>
  </div>

  <div class="abs" style="left:18px;top:200px">
    <div class="brand brand--lg">Orvida<small>accertamento danni elettrici</small></div>
    <p class="sub" style="margin-top:8px">Sinistri da<br>Fenomeno Elettrico</p>
    <ul class="list" style="margin-top:6px;width:150px">
      <li><b>I sinistri da "Fenomeno elettrico" sono gestiti con personale qualificato ed elettrotecnico interno</b></li>
      <li>l'accertamento tecnico e la riparazione dei beni vengono svolti sia in sede di sopralluogo che presso il ns. Laboratorio tecnico interno attrezzato.</li>
    </ul>
  </div>

  <div class="abs" style="left:198px;top:204px">
    <div class="brand brand--lg" style="letter-spacing:2px">VELARIS<small>claims services</small></div>
    <p class="sub" style="margin-top:10px">Servizi integrati</p>
    <ul class="list list--tight" style="margin-top:6px">
      <li>Teleclaimer</li><li>Crisis Management</li><li>Auditing</li><li>Energy Renewable</li>
      <li>A.P.R. (Drone)</li><li>Valutazione rischi</li><li>Tecnologici</li><li>Business Interruption</li>
    </ul>
  </div>

  <div class="badge" style="left:40px;top:372px;width:20px;height:20px;border-radius:50%"></div>
  <div class="badge" style="left:108px;top:372px;width:24px;height:20px"></div>
  <div class="badge" style="left:170px;top:374px;width:60px;height:16px"></div>
  <div class="badge" style="left:268px;top:372px;width:52px;height:20px"></div>

  <div class="footer-band"></div>
  <div class="addr" style="left:22px;top:424px"><b>SEDE OPERATIVA</b>Via Corvina 12 - 20100 Lorvano<br>Tel. 011/0000100 - Fax 011/0000101<br>info@vardanopescetti.example</div>
  <div class="addr" style="left:140px;top:424px"><b>SEDE SECONDARIA</b>Via Ardena 8 - 23000 Valmora<br>Tel. 011/0000200 - Fax 011/0000101<br>info@vardanopescetti.example</div>
  <div class="seal"></div>

  <div class="brand brand--lg abs" style="left:404px;top:45px">Vardano &amp; Pescetti<small>consulenza tecnica per le assicurazioni</small></div>
  <div class="brand abs" style="left:600px;top:48px;font-weight:700">T.R.V.</div>
  <div class="brand abs" style="left:668px;top:48px">Orvida</div>

  <div class="photo cover-photo" role="img" aria-label="Foto in bianco e nero di una calcolatrice con matita su documenti"></div>
  <div class="cover-text" style="left:408px;top:296px">PERIZIE ASSICURATIVE</div>
  <div class="cover-text" style="left:408px;top:324px">INDENNIZZO IN FORMA SPECIFICA</div>
  <div class="cover-text" style="left:408px;top:352px">ACCERTAMENTO DANNI DA<br>FENOMENO ELETTRICO</div>

  <div class="url" style="right:26px;top:443px">www.vardanopescetti.example</div>
  <div class="stripe"></div>
</section>

<!-- Inside spread: letter, clients, territory, office -->
<section class="spread spread--inside">
  <div class="fold"></div>

  <div class="brand abs" style="left:24px;top:14px;font-weight:700;font-size:9px">T.R.V.</div>
  <div class="brand abs" style="left:70px;top:14px;font-size:9px">Orvida</div>
  <div class="brand abs" style="left:260px;top:12px;font-size:11px">Vardano &amp; Pescetti<small>consulenza tecnica</small></div>

  <div class="letter">
    <p style="left:24px;top:12px;font-weight:700">Lorvano, 21 maggio 2018</p>
    <p style="left:250px;top:10px"><b>Egr.</b>&nbsp; Dott. Renato Valsesi<br>&nbsp;&nbsp;&nbsp;&nbsp;&nbsp;&nbsp; Oxtra Assicurazioni S.p.A.<br>&nbsp;&nbsp;&nbsp;&nbsp;&nbsp;&nbsp; Vs. Sede</p>
    <p style="left:24px;top:44px">Oggetto: Studio peritale Vardano e Pescetti S.r.l.</p>
    <p style="left:24px;top:60px;width:330px"><b style="color:var(--blue-deep)">Egregio Dott. Valsesi,</b><br>in qualità di Vs. Fiduciari sottoponiamo alla Vs. attenzione ns. sintetica presentazione circa le attività svolte dalla ns. Struttura.</p>
  </div>

  <h2 class="title abs" style="left:24px;top:152px;font-size:10px">LE MANDANTI</h2>
  <div class="insurers">
    <span>Alvenna</span><span>Oxtra</span><span>Sirella</span><span>Itavo</span>
    <span>Grendova</span><span>Realto Mutua</span><span>Pravia</span><span>Assivero</span>
    <span>Unvera</span><span>Valmora</span><span>Kesta</span><span>Italdora</span>
    <span></span><span>Genvaro</span><span>Ispera</span><span></span>
  </div>

  <div class="territory">
    <p>La Struttura opera su tutte le province della Lombardia, parte del Veneto ed Emilia Romagna, con attività per la gestione di sinistri Complessi su tutto il territorio nazionale.</p>
    <div class="map" style="left:126px;width:124px"><div role="img" aria-label="Mappa delle province della Lombardia suddivise per colore" style="background:linear-gradient(135deg,#b9d99a,#f1c27d 45%,#b7a6d6)"></div></div>
    <div class="map" style="left:256px;width:111px"><div role="img" aria-label="Mappa del Veneto con area evidenziata in giallo" style="background:linear-gradient(160deg,#eef3f7 40%,#ecec5a 70%,#d8e6f0)"></div></div>
  </div>

  <h2 class="title abs" style="left:398px;top:22px;font-size:10px">LO STUDIO</h2>
  <div class="photo" role="img" aria-label="Facciata dell'edificio della sede con parcheggio" style="left:398px;top:44px;width:155px;height:90px;background:linear-gradient(160deg,#8fb0d8,#c8a24a 55%,#6f6f6f)"></div>
  <div class="studio-note">
    <p>Lo studio ha sede in via Corvina 12 a Lorvano, in zona limitrofa al nodo autostradale, presso stabile direzionale. La zona è servita da ampio parcheggio per la ricezione del pubblico.</p>
    <p>La nostra sede si compone di spazi direzionali, operativi ed amministrativi dotati delle strumentazioni informatiche necessarie allo svolgimento dell'attività peritale.</p>
  </div>
  <div class="photo" role="img" aria-label="Ingresso dell'ufficio con piante e arredi" style="left:398px;top:144px;width:155px;height:100px;background:linear-gradient(160deg,#a8a39a,#5d5a55)"></div>
  <div class="photo" role="img" aria-label="Corridoio interno dell'ufficio" style="left:562px;top:144px;width:154px;height:100px;background:linear-gradient(160deg,#c9c7c2,#7d776f)"></div>
  <p class="body-small" style="left:398px;top:252px;width:320px">La struttura è dotata inoltre di un laboratorio tecnico interno ove il nostro personale specializzato effettua analisi sui reperti di sinistro in relazione a danni di natura elettrica/elettronica.</p>
  <div class="photo" role="img" aria-label="Sala riunioni dell'ufficio" style="left:398px;top:279px;width:96px;height:70px;background:linear-gradient(160deg,#9a9590,#4f4b47)"></div>
  <div class="photo" role="img" aria-label="Postazione di lavoro con scrivania" style="left:505px;top:279px;width:96px;height:70px;background:linear-gradient(160deg,#b8b4ae,#5a5550)"></div>
  <div class="photo" role="img" aria-label="Ufficio operativo con computer" style="left:612px;top:279px;width:101px;height:70px;background:linear-gradient(160deg,#a9a6a0,#55524e)"></div>
  <p class="body-small" style="left:398px;top:362px;width:100px">Ringraziando per l'attenzione prestata l'occasione è gradita per porgere cordiali saluti.</p>
  <div class="photo" role="img" aria-label="Laboratorio tecnico con banco di lavoro" style="left:505px;top:359px;width:208px;height:55px;background:linear-gradient(160deg,#8c8883,#3d3a37)"></div>

  <div class="brand brand--lg abs" style="left:398px;top:434px">Vardano &amp; Pescetti<small>consulenza tecnica per le assicurazioni</small></div>
  <div class="sign" style="left:546px;top:428px">Gianpaolo Vardano<i></i></div>
  <div class="sign" style="left:632px;top:428px">Marco Pescetti<i></i></div>

  <div class="stripe"></div>
</section>

</body>
</html>
```